Vantor Grid Advisory Partners - Website

Design & Build a website for a new company which operates in the Systems and Technology space for Transportation, Government and Commercial sectors.

Overall design should be minimalist in nature.
Should also have a feed that provides news and event updates on the main page.
Logo has already been awarded and should be incorporated into the site.

We like the overall layout, functionality and simplicity of the below sites. Submitted designs could be similar to or a combination of the aspects on these sites, or perhaps a whole different concept - we are open to new ideas.
Morqeli.com
Tumb.it

All I am moving away from the Tumb.it website and would like it to be more aligned with Morqeli.com not only in layout but in functionality. I will be extending the deadline of this design brief for two weeks to incorporate additional requirements and will add addtional funding to the project.

Apologies for not having more information available to provide but with so many submissions its getting confusing.

Thanks Dorian

Important: We will need two language versions of the website, English and Arabic; the website is hosted on HostPivo

Hello All, Thank you for your submissions. We have narrowed it down to the final 6 designers and I just wanted to take a moment and provide a bit of feedback regarding the concepts that we like and the modifications we are looking for. First, let me mention some of the design functions we like. - At the top of the homepage we really like the "region" or "language" tab so that the website can be viewed in both English and Arabic. - We like the homepage to have clear color variation so that the different sections of the homepage are distinct. Additionally, we like the bottom portion of the homepage to be in red. We feel that draws attention to our contact information. Again, we would like the colors to integrate black, gray-scale, red, etc. - Having a search tab at the top of the home page, or integrated into the main image, so that the site is easy to navigate. - We especially like the main image to have the scrolling tabs at the bottom so it is easy to browse the services offered (Consultancy, Solutions Architecture, Masters Systems Integration, Independent Design Review). - In regards to the services offered tab we really like the idea that a few people presented that have the outside of our logo with an icon in the middle of consultancy, solutions, etc., etc. Secondly, as mentioned in our brief we really enjoy the design of morqeli site. Specially, we enjoy the strong iconic images they use, the way the tabs at the top scroll easily, and contact us page that generates an email. Lastly, I've included some photos of the concept we have been working on. What we are trying to demonstrate is how our company offers a range of services that are essentially linked together. We provide individual services that when combined present the full service package. We would like this concept to be integrated into the over concept of our website. Please feel free to ask for clarification of any of the above points or contact us if you have any additional questions. We appreciate all of your hard work and are very excited to see the updated designs. Best, Miriam Okaford Vangridex Senior Program Manager miriam.okaford@vangridax.example

Industry/Entity Type

Government

Font styles to use
Serif
Sans Serif

Requirements
Must have
• Must work on/adapt to various/mobile devices (responsive)
Must be simple and straightforward
Colors should be in line/matching with logo
2 language versions: English and Arabic (no Thai)
Services should be the first group/row of items after/below the main image
Note: the website will be hosted by hostpivo
Nice to have
• Submit feedback form
What's New section
The banner at the bottom of the site should not be too large; we would like a narrow one more
It would be nice if the header/top banner (with Home, About, etc. tabs) could stay in place as you scroll down (like Morqeli and Chatterly)
We will likely only use one image with a Company slogan on the Home page rather than a carousel of images to rotate through
Should not have
• This is the existing website: http://www.vangridex.example
We do not like the animation, the way the banner icons/titles bounce
Not simple enough, we don't like the functionality or how pages load so slowly
We do not like the logo centered - it should be at the left
The banner and its tabs should not be towards the right, we would like them to be centered, to go all the way across and to be below the logo

```html
<!DOCTYPE html>
<html lang="en">
<head>
<meta charset="utf-8">
<title>Vangridex — Home</title>
<link href="https://fonts.googleapis.com/css2?family=Bebas+Neue&family=Oswald:wght@300;400;500&family=Open+Sans:wght@400;600&display=swap" rel="stylesheet">
<style>
:root{
  --red:#a0403c;
  --red-dark:#8c3431;
  --ink:#222222;
  --text:#444444;
  --muted:#777777;
  --rule:#9a9a9a;
  --grey-band:#8b8b8b;
  --light:#ededed;
  --footer:#4a4a4a;
  --white:#ffffff;
  --gold:#d6a21f;
}
*{margin:0;padding:0;box-sizing:border-box}
html,body{width:1200px;height:2536px;overflow:hidden}
body{position:relative;background:var(--white);font-family:"Oswald",sans-serif;color:var(--text)}
.abs{position:absolute}
.heading{font-family:"Bebas Neue",sans-serif;font-weight:400;letter-spacing:.5px;color:var(--ink)}
.body-copy{font-family:"Oswald",sans-serif;font-weight:300;text-transform:uppercase;color:var(--text)}
.section-rule{position:absolute;left:244px;width:730px;height:1px;background:var(--rule)}

/* header */
.site-header{top:0;left:0;width:1200px;height:86px;background:var(--white)}
.brand{left:249px;top:16px;display:flex;align-items:center;gap:8px}
.brand-mark{width:14px;height:14px;background:var(--ink)}
.brand-name{font-family:"Bebas Neue",sans-serif;font-size:26px;color:var(--ink);letter-spacing:2px}
.lang-switch{left:636px;top:13px;font-family:"Oswald",sans-serif;font-size:10px;color:var(--ink);font-weight:500}
.search-box{left:791px;top:8px;width:183px;height:22px;border:1px solid #bdbdbd;background:#f3f3f3}
.main-nav{left:466px;top:50px;display:flex;align-items:center;gap:22px;font-family:"Bebas Neue",sans-serif;font-size:15px;color:var(--ink)}
.main-nav .active{border-bottom:1px solid var(--ink)}
.main-nav .sep{font-size:10px;color:#999}

/* hero */
.hero{top:86px;left:0;width:1200px;height:509px;background:linear-gradient(100deg,#eef0f1 0%,#dfe2e4 35%,#c9c6c0 60%,#a8a39a 80%,#8b877f 100%)}
.hero-hex{left:0;top:0}
.hero-title{left:471px;width:258px;text-align:center;font-family:"Bebas Neue",sans-serif;color:var(--ink)}

/* about */
.about-copy{left:244px;top:645px;width:730px;font-size:12px;line-height:17px}
.about-copy strong{font-weight:500;color:var(--ink)}

/* services */
.services{top:769px;left:0;width:1200px;height:260px;background:var(--red)}
.service-card{left:296px;top:55px;width:124px;height:186px;background:var(--white);box-shadow:0 2px 4px rgba(0,0,0,.25)}
.service-label{top:126px;width:130px;text-align:center;font-family:"Oswald",sans-serif;font-weight:300;font-size:15px;text-transform:uppercase;color:var(--white)}
.service-card .service-label{color:var(--ink)}
.service-tagline{top:104px;left:0;width:124px;text-align:center;font-family:"Bebas Neue",sans-serif;font-size:18px;line-height:21px;color:var(--ink)}

/* events */
.feature-photo{left:249px;top:1080px;width:188px;height:138px;background:linear-gradient(135deg,#c9b79a,#7b6a58 60%,#3d3a3a)}
.feature-title{left:447px;top:1086px;font-size:20px;color:var(--ink)}
.feature-copy{left:447px;top:1107px;width:530px;font-size:10.5px;line-height:14.5px;color:var(--muted)}
.read-more{left:445px;top:1175px;width:82px;height:20px;background:var(--red);color:var(--white);font-family:"Bebas Neue",sans-serif;font-size:15px;text-align:center;line-height:21px}
.event-card{top:1233px;width:170px;height:190px;border:1px solid #c8c8c8;background:var(--white);box-shadow:0 1px 3px rgba(0,0,0,.2)}
.event-photo{position:absolute;left:4px;top:16px;width:160px;height:92px}
.event-title{position:absolute;left:4px;top:114px;font-size:15px;white-space:nowrap}
.event-copy{position:absolute;left:4px;top:132px;width:162px;font-size:8px;line-height:11px}

/* news */
.news{top:1462px;left:0;width:1200px;height:358px;background:var(--grey-band)}
.news .section-rule{background:#d0d0d0}
.news-icon{left:249px;width:85px;height:84px;background:var(--white);border-radius:6px;box-shadow:0 1px 3px rgba(0,0,0,.3)}
.news-title{left:340px;font-size:17px;color:var(--white)}
.news-copy{left:340px;width:162px;font-size:9px;line-height:12px;color:var(--white)}
.news-more{left:492px;width:13px;height:13px;border:1px solid var(--white);border-radius:50%;color:var(--white);font-size:11px;line-height:10px;text-align:center}
.blog-panel{left:543px;top:55px;width:436px;height:277px;border-radius:6px;background:radial-gradient(ellipse at 40% 50%,#d9c39a 0%,#b89868 45%,#7d6a4c 100%);box-shadow:0 2px 5px rgba(0,0,0,.35)}

/* locations */
.locations-copy{left:244px;top:1860px;width:730px;font-size:11px;line-height:14.5px}
.office-name{font-family:"Bebas Neue",sans-serif;font-size:22px;color:var(--ink)}
.office-address{font-size:10.5px;line-height:13px}

/* contact */
.contact{top:2069px;left:0;width:1200px;height:340px;background:var(--light)}
.field{left:352px;width:246px;height:24px;background:var(--white);border:1px solid #d4d4d4;font-family:"Open Sans",sans-serif;font-size:10px;color:#555;padding-left:26px;line-height:22px}
.field-icon{position:absolute;left:8px;top:7px;width:10px;height:8px;background:#8aa0b8}
.field.subject{background:#fbe3e3;border-color:#e8b5b5;color:#b33;font-weight:600}
.field.message{height:158px;padding-left:6px;line-height:18px}
.send-btn{left:352px;top:2362px;width:246px;height:24px;background:linear-gradient(#f8f8f8,#dcdcdc);border:1px solid #c4c4c4;font-family:"Open Sans",sans-serif;font-size:10px;font-weight:600;color:#444;text-align:center;line-height:22px}
.map-area{left:607px;top:34px;width:322px;height:242px;border:1px solid #d0d0d0;background:linear-gradient(135deg,#ecebe4,#dcdad0 50%,#e6e3d6)}
.follow-label{left:614px;top:2358px;font-size:26px;color:var(--ink)}
.social-name{top:2366px;font-family:"Oswald",sans-serif;font-weight:400;font-size:13px;color:var(--red)}

/* footer */
.site-footer{top:2409px;left:0;width:1200px;height:127px;background:var(--footer)}
.footer-links{left:277px;top:20px;font-family:"Bebas Neue",sans-serif;font-size:15px;line-height:16.5px;color:var(--white)}
.copyright{left:648px;top:80px;font-family:"Bebas Neue",sans-serif;font-size:21px;color:var(--white)}
</style>
</head>
<body>

<header class="site-header abs">
  <div class="brand abs"><span class="brand-mark"></span><span class="brand-name">VANGRIDEX</span></div>
  <div class="lang-switch abs">ENGLISH VERSION | النسخة العربية</div>
  <div class="search-box abs">
    <svg class="abs" style="right:6px;top:3px" width="14" height="14" viewBox="0 0 14 14"><circle cx="5.5" cy="5.5" r="4" fill="none" stroke="#999" stroke-width="1.5"/><line x1="8.5" y1="8.5" x2="13" y2="13" stroke="#999" stroke-width="1.5"/></svg>
  </div>
  <nav class="main-nav abs">
    <span class="active">HOME</span><span class="sep">✧</span>
    <span>ABOUT US</span><span class="sep">✧</span>
    <span>OUR SERVICES</span><span class="sep">✧</span>
    <span>NEWS</span><span class="sep">✧</span>
    <span>LOCATIONS</span><span class="sep">✧</span>
    <span>BUSINESS UNITS</span>
  </nav>
</header>

<section class="hero abs" role="img" aria-label="Photo of a business team planning together at a glass board">
  <svg class="hero-hex abs" width="1200" height="509" viewBox="0 0 1200 509">
    <polygon points="600,93 729,165 729,310 600,382 471,310 471,165" fill="#f7f7f7"/>
    <polygon points="559,301 645,301 645,352 602,378 559,352" fill="#333333"/>
    <polyline points="559,360 602,386 645,360" fill="none" stroke="#333333" stroke-width="3"/>
  </svg>
  <div class="hero-title abs" style="top:207px;font-size:27px;font-weight:400;color:#555">WE OFFER YOU</div>
  <div class="hero-title abs" style="top:232px;font-size:32px">RELIABLE SOLUTIONS</div>
  <div class="hero-title abs" style="top:307px;font-size:15px;color:#fff">START</div>
  <div class="hero-title abs" style="top:320px;font-size:29px;color:#fff">NOW</div>
</section>

<section class="about">
  <div class="section-rule" style="top:616px"></div>
  <h2 class="heading abs" style="left:244px;top:621px;font-size:17px">ABOUT US</h2>
  <p class="about-copy body-copy abs">We specialize in delivering quality professional services and technical projects that support larger business goals. We understand that most technical projects are conceptualized to support a larger vision with actual business goals in mind and ensure that all of our professional and certified expertise is included in our professional ded in our professional services to meet those goals.<br><br>Our ultimate goal is to provide quality, technical and professional services on projects of any scale and/or complexity, from conception through to completion. Our philosophy is simple: <strong>stick to what you are good at and be the best at it.</strong></p>
</section>

<section class="services abs">
  <div class="section-rule" style="top:13px;background:#d99a97"></div>
  <h2 class="heading abs" style="left:244px;top:18px;font-size:18px;color:#fff">OUR SERVICES</h2>
  <div class="service-card abs">
    <svg class="abs" style="left:44px;top:16px" width="36" height="36" viewBox="0 0 36 36" fill="none" stroke="#444" stroke-width="1.4"><rect x="6" y="4" width="20" height="26"/><line x1="10" y1="11" x2="22" y2="11"/><line x1="10" y1="16" x2="22" y2="16"/><line x1="10" y1="21" x2="18" y2="21"/><line x1="20" y1="28" x2="32" y2="10"/></svg>
    <div class="service-label abs" style="left:-3px;top:70px">CONSULTING</div>
    <div class="service-tagline abs">LET'S<br>DELIBERATE<br>TOGETHER.</div>
  </div>
  <svg class="abs" style="left:455px;top:74px" width="32" height="36" viewBox="0 0 32 36" fill="none" stroke="#fff" stroke-width="1.4"><circle cx="16" cy="13" r="9"/><path d="M12 22v5h8v-5"/><line x1="12" y1="30" x2="20" y2="30"/></svg>
  <div class="service-label abs" style="left:406px">ENGINEERING</div>
  <svg class="abs" style="left:577px;top:74px" width="32" height="36" viewBox="0 0 32 36" fill="none" stroke="#fff" stroke-width="1.4"><ellipse cx="16" cy="7" rx="11" ry="4"/><path d="M5 7v20c0 2 5 4 11 4s11-2 11-4V7"/><path d="M5 14c0 2 5 4 11 4s11-2 11-4"/><path d="M5 21c0 2 5 4 11 4s11-2 11-4"/></svg>
  <div class="service-label abs" style="left:528px">CONSTRUCTION</div>
  <svg class="abs" style="left:697px;top:72px" width="36" height="38" viewBox="0 0 36 38" fill="none" stroke="#fff" stroke-width="1.4"><rect x="4" y="4" width="28" height="20"/><line x1="18" y1="24" x2="18" y2="30"/><line x1="10" y1="31" x2="26" y2="31"/></svg>
  <div class="service-label abs" style="left:650px">OPERATIONS</div>
  <svg class="abs" style="left:816px;top:72px" width="38" height="38" viewBox="0 0 38 38" fill="none" stroke="#fff" stroke-width="1.6"><line x1="6" y1="32" x2="30" y2="8"/><circle cx="31" cy="7" r="4"/><line x1="8" y1="6" x2="32" y2="30"/><rect x="4" y="3" width="6" height="6"/></svg>
  <div class="service-label abs" style="left:769px">MAINTENANCE</div>
</section>

<section class="events">
  <div class="section-rule" style="top:1047px"></div>
  <h2 class="heading abs" style="left:249px;top:1052px;font-size:18px">UPCOMING EVENTS</h2>
  <div class="feature-photo abs" role="img" aria-label="Photo of two delegates shaking hands at a conference"></div>
  <h3 class="feature-title heading abs">VANGRIDEX IN GLOBAL ENERGY SYSTEMS FORUM IN BEIJING</h3>
  <p class="feature-copy body-copy abs">Lorem ipsum dolor sit amet, consectetur adipisicing elit, sed do eiusmod tempor incididunt ut labore et dolore magna aliqua. Ut enim ad minim veniam, quis nostrud exercitation ullamco laboris nisi ut aliquip ex ea commodo consequat. Duis aute irure dolor in reprehenderit in voluptate velit esse cillum dolore eu fugiat nulla pariatur. Excepteur sint occaecat cupidatat non proident, sunt in culpa qui officia deserunt mollit anim id est laborum.</p>
  <div class="read-more abs">READ MORE</div>

  <article class="event-card abs" style="left:248px">
    <div class="event-photo" role="img" aria-label="Photo of a conference hall with seated audience" style="background:linear-gradient(#6b4a2a,#c58a3c 55%,#3a2a1e)"></div>
    <h4 class="event-title heading">DOHA'S EVENTS</h4>
    <p class="event-copy body-copy">Across the region were deliberated at a 'safety design in web application' conference in Doha yesterday.</p>
  </article>
  <article class="event-card abs" style="left:426px">
    <div class="event-photo" role="img" aria-label="Photo of a crowd at an exhibition stand" style="background:linear-gradient(#b9cbd6,#5f7c8e 55%,#2f3b45)"></div>
    <h4 class="event-title heading">VANGRIDEX FIRST STEP IN UK</h4>
    <p class="event-copy body-copy">Across the region were deliberated at a 'safety design in web application' conference in Doha yesterday.</p>
  </article>
  <article class="event-card abs" style="left:609px">
    <div class="event-photo" role="img" aria-label="Photo of a panel seated on a stage" style="background:linear-gradient(#2a2f55,#7a5a3c 55%,#c99a5a)"></div>
    <h4 class="event-title heading">VANGRIDEX'S ASIA PARTNERSHIP</h4>
    <p class="event-copy body-copy">Across the region were deliberated at a 'safety design in web application' conference in Doha yesterday.</p>
  </article>
  <article class="event-card abs" style="left:789px">
    <div class="event-photo" role="img" aria-label="Photo of a panel seated on a stage" style="background:linear-gradient(#2a2f55,#7a5a3c 55%,#c99a5a)"></div>
    <h4 class="event-title heading">VANGRIDEX'S ASIA PARTNERSHIP</h4>
    <p class="event-copy body-copy">Across the region were deliberated at a 'safety design in web application' conference in Doha yesterday.</p>
  </article>
</section>

<section class="news abs">
  <div class="section-rule" style="top:15px"></div>
  <h2 class="heading abs" style="left:249px;top:22px;font-size:18px;color:#fff">NEWS</h2>

  <div class="news-icon abs" style="top:55px">
    <div class="abs" role="img" aria-label="Line drawing of a business person" style="left:22px;top:16px;width:40px;height:52px;background:#e2e2e2;border-radius:4px"></div>
  </div>
  <h3 class="news-title heading abs" style="top:60px">VANGRIDEX SPREADS IN CHINA</h3>
  <p class="news-copy body-copy abs" style="top:78px">It is a long established fact that a reader will be distracted by the readable content of a page when looking at its layout.</p>
  <div class="news-more abs" style="top:121px">+</div>

  <div class="news-icon abs" style="top:151px">
    <svg class="abs" style="left:20px;top:17px" width="46" height="50" viewBox="0 0 46 50" fill="none" stroke="#333" stroke-width="1.4"><circle cx="22" cy="26" r="18"/><path d="M22 26V8"/><path d="M22 26l14 11"/><path d="M26 4a18 18 0 0 1 16 16H26z"/></svg>
  </div>
  <h3 class="news-title heading abs" style="top:156px">VANGRIDEX SPREADS IN CHINA</h3>
  <p class="news-copy body-copy abs" style="top:174px">It is a long established fact that a reader will be distracted by the readable content of a page when looking at its layout.</p>
  <div class="news-more abs" style="top:217px">+</div>

  <div class="news-icon abs" style="top:251px">
    <svg class="abs" style="left:22px;top:14px" width="42" height="54" viewBox="0 0 42 54" fill="none" stroke="#333" stroke-width="1.4"><line x1="4" y1="50" x2="38" y2="50"/><rect x="8" y="34" width="6" height="16"/><rect x="18" y="24" width="6" height="26"/><rect x="28" y="14" width="6" height="36"/><polyline points="6,26 16,16 24,18 36,4"/></svg>
  </div>
  <h3 class="news-title heading abs" style="top:250px">VANGRIDEX SPREADS IN CHINA</h3>
  <p class="news-copy body-copy abs" style="top:268px">It is a long established fact that a reader will be distracted by the readable content of a page when looking at its layout.</p>
  <div class="news-more abs" style="top:312px">+</div>

  <div class="blog-panel abs" role="img" aria-label="Blurred photo backdrop for the blog feed">
    <svg class="abs" style="left:0;top:0" width="436" height="277" viewBox="0 0 436 277">
      <polygon points="214,53 291,97 291,185 214,229 137,185 137,97" fill="var(--gold)"/>
    </svg>
    <div class="abs heading" style="left:164px;top:82px;width:100px;text-align:center;font-size:40px;line-height:38px;color:#fff">RSS<br><span style="color:#f0d88a">OR</span><br>BLOG</div>
  </div>
</section>

<section class="locations">
  <div class="section-rule" style="top:1834px"></div>
  <h2 class="heading abs" style="left:249px;top:1838px;font-size:18px">LOCATIONS</h2>
  <p class="locations-copy body-copy abs">We are a systems architecture, project/construction management and consultancy firm, based in Bangkok, Thailand, with offices opening in the Middle East in the near future specializing in project and construction management, engineering, design services and turn-key solutions for technical systems for projects. Vangridex focus is on providing quality systems design, construction and integration, using recognized international industry standards and codes for every project we deliver.</p>

  <svg class="abs" style="left:370px;top:1960px" width="34" height="54" viewBox="0 0 34 54" fill="none" stroke="#333" stroke-width="1.4"><path d="M17 52C8 36 3 26 3 17a14 14 0 0 1 28 0c0 9-5 19-14 35z"/><circle cx="17" cy="17" r="5"/></svg>
  <div class="office-name abs" style="left:349px;top:2028px">BANGKOK</div>
  <p class="office-address body-copy abs" style="left:435px;top:1986px">14 Soi Lumpini 7<br>Khlong Toei Bangkok<br>Thailand</p>

  <div class="abs" role="img" aria-label="Hand-drawn globe illustration" style="left:652px;top:1952px;width:64px;height:64px;border-radius:50%;background:#dcdcdc"></div>
  <div class="office-name abs" style="left:636px;top:2026px">MIDDLE EAST</div>
  <p class="office-address body-copy abs" style="left:770px;top:1994px">Your adresses go here</p>
</section>

<section class="contact abs">
  <div class="field abs" style="top:32px;color:#aaa"><span class="field-icon"></span>Name</div>
  <div class="field abs" style="top:63px"><span class="field-icon"></span>User input</div>
  <div class="field subject abs" style="top:94px"><span class="field-icon" style="background:#c55"></span>Subject</div>
  <div class="field message abs" style="top:125px;color:#888">Message</div>
  <div class="map-area abs" role="img" aria-label="Street map of the Bangkok office area"></div>
</section>
<div class="send-btn abs">Send Message</div>
<div class="follow-label heading abs">FOLLOW US ON</div>
<span class="social-name abs" style="left:770px">Plusora</span>
<span class="social-name abs" style="left:826px">Chatterly</span>
<span class="social-name abs" style="left:888px">Chirpwell</span>

<footer class="site-footer abs">
  <nav class="footer-links abs">HOME<br>ABOUT US<br>OUR SERVICES<br>NEWS<br>LOCATIONS BUSINESS UNITS</nav>
  <div class="copyright abs">ALL COPYRIGHT IS RESERVED. VANGRIDEX TECHNOLOGY INC.</div>
</footer>

</body>
</html>
```